Creative UI design for web application

I need a new UI design for my web application. It will be used by small and micro business owners to plan & implement growth tactics.

I've attached the current design (which I'm open to be changed) - but in particular I need to design the centre of the screen, where the work actually happens.

There needs to be place for a title (YOUR BUSINESS) and description (say 1-2 paragraphs of text) - and am happy to include icons or imagery where makes sense. It may make sense for the user to be able to upload their business logo and name, for example.

This screen will be used by the business owner to understand the real value they offer potential customers and their point of difference - why they exist and why potential customers should care.

They'll use the information they put into this screen to plan things like their messaging.

Following that, there needs to be 2 sections in the dashboard.

The first section is titled "WHO YOU ARE"

The first section will include a number of boxes that the user can input information into, as follows:

- Logo
- Business name
- Business tag line
- Business vision
- Business bio
- Brand colours (these should end up as swatches based on the colour code they enter) - the colour code for each colour swatch should also be visible.
- Key competitors
- SWOT analysis (boxes to enter their strengths, weaknesses, opportunities and threats).

The second section is titled "WHY YOU EXIST"

The second section will include a number of boxes that the user can input information (text) into, as follows:

- Who are your ideal customers?
- What problem are you trying to solve for them?
- What pain points will this remove for them?
- How do you solve it?
- How else could this problem be solved?
- Who offers these other solutions?
- Why is your solution better?
- How much does your solution cost?
- What value are you providing to justify this cost?
- How will this make their life/job easier/better?

They should be able to write a decent amount of information in the boxes.

There should ideally be a place for a description for each of these text fields (for both section 1 & 2) as well so I can give them a little bit more direction around what to put in the box. Alternatively there could be a little icon (say a question mark or "i") that they could click on to view instructions. The instructions will be around 2-4 sentences long for each text field.

You have 2 options:

a) This all needs to appear on the one screen, and the navigation needs to be visible (as per the example attached but feel free to recreate this navigation)

Note: the page can scroll below the fold - but please provide the design for the full length of the page.

b) Potentially the 2 sections could actually be in 2 different items in the menu - YOUR BUSINESS and YOUR VALUE (which would sit next to YOUR BUSINESS and before YOUR CUSTOMER in the screenshot provided). feel free to design them as 2 separate screens if you prefer.

I have attached a screenshot of the app as it stands today (screen shot 2017) which would still exist in the new design but under a different section (the learn section from the plan2 mockup attached)

I have mocked up how this new screen could look if broken into 2 and that's also attached. If you can make this come to life - and look more engaging that would be helpful! :)

Target Market(s)

Small and micro business owners

Industry/Entity Type

Marketing

Number of Pages Required

1 page

Font styles to use
Sans Serif
Other font styles liked:
• Montserrat

Colors
87cfc6
d2a4cc
ffffff
85cae6
e8e8e8
5c5c5c

Requirements
Must have
• Use of my brand colours: #cc8eb2, #76d6c8, #68c7ff as well as white and #595959. Must be visually pleasing / engaging, designed for desktop (as it's a desktop application), really easy to use / navigate.
• Use font Montserrat light & Montserrat Regular or Bold. Mostly should be Montserrat light.
Nice to have
• Would be nice to see how this would look on mobile (as the application is responsive) but this is not mandatory.
Should not have
• Should not look too corporate or dry.

```html
<!DOCTYPE html>
<html lang="en">
<head>
<meta charset="utf-8">
<title>Leafline – Your Business</title>
<link href="https://fonts.googleapis.com/css2?family=Montserrat:wght@300;400;500;600;700&display=swap" rel="stylesheet">
<style>
:root{
  --bar:#3b3b3b;
  --teal:#76d6c8;
  --pink:#cc8eb2;
  --blue:#68c7ff;
  --text:#595959;
  --dark:#333;
  --sub:#e0e0e0;
  --field:#ebebeb;
  --panel-head:#dedede;
  --line:#dadada;
  --white:#fff;
}
*{box-sizing:border-box;margin:0;padding:0}
html,body{width:1069px;height:1200px;overflow:hidden;background:var(--white)}
body{font-family:"Montserrat",sans-serif;font-weight:300;color:var(--text)}
.page{width:1300px;height:1459px;transform:scale(.8223);transform-origin:0 0;position:relative}
.topbar{height:58px;background:var(--bar);position:relative}
.brand{position:absolute;left:20px;top:24px;font-size:22px;font-weight:500;color:var(--white);letter-spacing:-.5px}
.main-nav{position:absolute;left:245px;top:8px;display:flex;height:50px}
.main-nav a{display:flex;align-items:center;padding:0 20px;color:var(--white);font-weight:600;font-size:15px;text-decoration:none;letter-spacing:.3px}
.main-nav a.active{background:var(--teal)}
.user-nav{position:absolute;right:0;top:0;height:58px;display:flex}
.user-nav a{display:flex;align-items:center;gap:6px;padding:0 14px;border-left:1px solid #555;color:var(--white);font-weight:600;font-size:15px;text-decoration:none}
.sub-nav{height:44px;background:var(--sub);border-bottom:1px solid #ccc;padding-left:245px;display:flex}
.sub-nav a{display:flex;align-items:center;padding:0 19px;border-right:1px solid #c8c8c8;font-weight:500;font-size:15px;color:#444;text-decoration:none;letter-spacing:.3px}
.sub-nav a.active{background:var(--pink);color:var(--white);border-right:none}
.intro{padding:22px 17px 0;font-size:16px;line-height:24px;width:1290px}
.intro p+p{margin-top:24px}
.panel{position:absolute;top:376px;width:615px;height:1002px;border:1px solid var(--line);border-top:none}
.panel.who{left:20px}
.panel.why{left:665px}
.panel h2{height:51px;background:var(--panel-head);padding:0 21px;display:flex;align-items:center;font-size:22px;font-weight:600;color:var(--dark);letter-spacing:.5px}
.panel-body{padding:14px 19px 0}
.field{height:87px;position:relative}
.field label,.block-label{display:block;font-size:16px;height:33px;padding-top:2px}
.input{height:40px;background:var(--field)}
.why .input{width:545px}
.info{position:absolute;right:0;top:48px}
.logo-row{display:flex;gap:10px}
.logo-row .input{flex:1}
.upload{width:95px;height:40px;background:var(--blue);color:var(--white);font-size:16px;font-weight:400;display:flex;align-items:center;justify-content:center}
.colour-row{display:flex;gap:10px}
.picker-btn{width:40px;height:40px;background:var(--field);display:flex;align-items:center;justify-content:center}
.colour-row .input{flex:1;display:flex;align-items:center;padding-left:12px;font-size:16px;color:var(--text)}
.swatches{position:absolute;left:25px;top:579px;width:219px;height:121px;background:var(--white);border:1px solid #ccc;box-shadow:0 1px 3px rgba(0,0,0,.1);padding:12px 11px;display:grid;grid-template-columns:repeat(6,26px);gap:8px;z-index:2}
.swatches span{width:26px;height:26px;border:2px solid var(--white);outline:1px solid #ccc}
.brand-chips{position:absolute;left:262px;top:591px;width:333px;height:40px;display:flex;justify-content:space-between;align-items:center}
.chip{display:flex;align-items:center;gap:6px;font-size:13px;font-weight:400;color:var(--text)}
.chip i{display:block;width:24px;height:24px;border:1px solid #ccc}
.competitors{position:absolute;left:19px;top:706px;width:575px}
.swot{position:absolute;left:19px;top:793px;width:575px}
.swot-grid{display:grid;grid-template-columns:1fr 1fr;gap:8px}
.swot-grid div{height:46px;background:var(--field);padding:13px 12px;font-size:14px;color:#8a8a8a}
.submit{position:absolute;left:470px;top:942px;width:124px;height:40px;background:var(--teal);color:var(--white);font-weight:600;font-size:15px;letter-spacing:.5px;display:flex;align-items:center;justify-content:center}
.footer{position:absolute;left:0;top:1409px;width:1300px;height:50px;background:#dcdcdc;display:flex;align-items:center;justify-content:center;font-size:15px;color:#444}
</style>
</head>
<body>
<div class="page">
  <header class="topbar">
    <div class="brand">LEAFLINE</div>
    <nav class="main-nav">
      <a class="active">PLAN</a><a>LEARN</a><a>REMEMBER</a>
    </nav>
    <nav class="user-nav">
      <a><svg width="16" height="18" viewBox="0 0 16 18" fill="none" stroke="#fff" stroke-width="1.6"><circle cx="8" cy="5" r="4"/><path d="M1 17c0-4 3-6 7-6s7 2 7 6"/></svg>My Profile</a>
      <a><svg width="20" height="20" viewBox="0 0 20 20" fill="none" stroke="#fff" stroke-width="1.8"><path d="M14 4.5A8 8 0 1 0 14 15.5"/><path d="M8 10h11M15 6l4 4-4 4"/></svg>Log out</a>
    </nav>
  </header>
  <nav class="sub-nav">
    <a class="active">YOUR BUSINESS</a><a>YOUR CUSTOMERS</a><a>YOUR GOALS</a><a>YOUR PLAN</a>
  </nav>
  <section class="intro">
    <p>Lorem ipsum dolor sit amet, consectetur adipiscing elit, sed do eiusmod tempor incididunt ut labore et dolore magna aliqua. Ut enim ad minim veniam, quis nostrud exercitation ullamco laboris nisi ut aliquip ex ea commodo consequat. Duis aute irure dolor in reprehenderit in voluptate velit esse cillum dolore eu fugiat nulla pariatur. Excepteur sint occaecat cupidatat non proident, sunt in culpa qui officia deserunt mollit anim id est laborum. Duis aute irure dolor in reprehenderit in voluptate velit esse cillum dolore eu fugiat nulla pariatur. Excepteur sint occaecat cupidatat non proident, sunt in culpa qui officia deserunt mollit anim id est laborum.</p>
    <p>Lorem ipsum dolor sit amet, consectetur adipiscing elit, sed do eiusmod tempor incididunt ut labore et dolore magna aliqua. Ut enim ad minim veniam, quis nostrud exercitation ullamco laboris nisi ut aliquip ex ea commodo consequat. Lorem ipsum dolor sit amet, consectetur adipiscing elit, sed do eiusmod tempor incididunt ut labore et dolore magna aliqua. Ut enim ad minim veniam, quis nostrud exercitation ullamco laboris nisi ut aliquip ex ea commodo consequat.</p>
  </section>

  <section class="panel who">
    <h2>WHO YOU ARE</h2>
    <div class="panel-body">
      <div class="field"><label>Logo</label><div class="logo-row"><div class="input"></div><div class="upload">Upload</div></div></div>
      <div class="field"><label>Business Name</label><div class="input"></div></div>
      <div class="field"><label>Business Tag Line</label><div class="input"></div></div>
      <div class="field"><label>Business Vision</label><div class="input"></div></div>
      <div class="field"><label>Business Bio</label><div class="input"></div></div>
      <div class="field"><label>Brand Colours</label>
        <div class="colour-row">
          <div class="picker-btn"><svg width="22" height="22" viewBox="0 0 22 22"><rect x="1" y="1" width="6" height="6" fill="#f5a"/><rect x="8" y="1" width="6" height="6" fill="#f99"/><rect x="15" y="1" width="6" height="6" fill="#c6c"/><rect x="1" y="8" width="6" height="6" fill="#fc4"/><rect x="8" y="8" width="6" height="6" fill="#9cf"/><rect x="15" y="8" width="6" height="6" fill="#c8f"/><rect x="1" y="15" width="6" height="6" fill="#6c6"/><rect x="8" y="15" width="6" height="6" fill="#4cd"/><rect x="15" y="15" width="6" height="6" fill="#88f"/></svg></div>
          <div class="input">#333555</div>
        </div>
      </div>
    </div>
    <div class="swatches">
      <span style="background:#ff5252"></span><span style="background:#536dfe"></span><span style="background:#18ffff"></span><span style="background:#69f0ae"></span><span style="background:#ffff00"></span><span style="background:#ffab40"></span>
      <span style="background:#ff1744"></span><span style="background:#3d5afe"></span><span style="background:#00e5ff"></span><span style="background:#00e676"></span><span style="background:#ffea00"></span><span style="background:#ff9100"></span>
      <span style="background:#d50000"></span><span style="background:#304ffe"></span><span style="background:#00b8d4"></span><span style="background:#00c853"></span><span style="background:#ffd600"></span><span style="background:#ff6d00"></span>
    </div>
    <div class="brand-chips">
      <span class="chip"><i style="background:#333555"></i>#333555</span>
      <span class="chip"><i style="background:#76d6c8"></i>#76D6C8</span>
      <span class="chip"><i style="background:#cc8eb2"></i>#CC8EB2</span>
    </div>
    <div class="competitors"><label class="block-label">Key Competitors</label><div class="input"></div></div>
    <div class="swot">
      <span class="block-label">SWOT Analysis</span>
      <div class="swot-grid">
        <div>Strengths</div><div>Weaknesses</div><div>Opportunities</div><div>Threats</div>
      </div>
    </div>
    <div class="submit">SUBMIT</div>
  </section>

  <section class="panel why">
    <h2>WHY YOU EXIST</h2>
    <div class="panel-body">
      <div class="field"><label>Who are your ideal customers?</label><div class="input"></div><svg class="info" width="22" height="22" viewBox="0 0 22 22"><circle cx="11" cy="11" r="11" fill="#bdbdbd"/><circle cx="11" cy="6" r="1.6" fill="#fff"/><path d="M9 9.5h3v7h1.5" stroke="#fff" stroke-width="2" fill="none"/></svg></div>
      <div class="field"><label>What problem are you trying to solve for them?</label><div class="input"></div><svg class="info" width="22" height="22" viewBox="0 0 22 22"><circle cx="11" cy="11" r="11" fill="#bdbdbd"/><circle cx="11" cy="6" r="1.6" fill="#fff"/><path d="M9 9.5h3v7h1.5" stroke="#fff" stroke-width="2" fill="none"/></svg></div>
      <div class="field"><label>What pain points will this remove for them?</label><div class="input"></div><svg class="info" width="22" height="22" viewBox="0 0 22 22"><circle cx="11" cy="11" r="11" fill="#bdbdbd"/><circle cx="11" cy="6" r="1.6" fill="#fff"/><path d="M9 9.5h3v7h1.5" stroke="#fff" stroke-width="2" fill="none"/></svg></div>
      <div class="field"><label>How do you solve it?</label><div class="input"></div><svg class="info" width="22" height="22" viewBox="0 0 22 22"><circle cx="11" cy="11" r="11" fill="#bdbdbd"/><circle cx="11" cy="6" r="1.6" fill="#fff"/><path d="M9 9.5h3v7h1.5" stroke="#fff" stroke-width="2" fill="none"/></svg></div>
      <div class="field"><label>How else could this problem be solved?</label><div class="input"></div><svg class="info" width="22" height="22" viewBox="0 0 22 22"><circle cx="11" cy="11" r="11" fill="#bdbdbd"/><circle cx="11" cy="6" r="1.6" fill="#fff"/><path d="M9 9.5h3v7h1.5" stroke="#fff" stroke-width="2" fill="none"/></svg></div>
      <div class="field"><label>Who offers these other solutions?</label><div class="input"></div><svg class="info" width="22" height="22" viewBox="0 0 22 22"><circle cx="11" cy="11" r="11" fill="#bdbdbd"/><circle cx="11" cy="6" r="1.6" fill="#fff"/><path d="M9 9.5h3v7h1.5" stroke="#fff" stroke-width="2" fill="none"/></svg></div>
      <div class="field"><label>Why is your solution better?</label><div class="input"></div><svg class="info" width="22" height="22" viewBox="0 0 22 22"><circle cx="11" cy="11" r="11" fill="#bdbdbd"/><circle cx="11" cy="6" r="1.6" fill="#fff"/><path d="M9 9.5h3v7h1.5" stroke="#fff" stroke-width="2" fill="none"/></svg></div>
      <div class="field"><label>How much does your solution cost?</label><div class="input"></div><svg class="info" width="22" height="22" viewBox="0 0 22 22"><circle cx="11" cy="11" r="11" fill="#bdbdbd"/><circle cx="11" cy="6" r="1.6" fill="#fff"/><path d="M9 9.5h3v7h1.5" stroke="#fff" stroke-width="2" fill="none"/></svg></div>
      <div class="field"><label>What value are you providing to justify this cost?</label><div class="input"></div><svg class="info" width="22" height="22" viewBox="0 0 22 22"><circle cx="11" cy="11" r="11" fill="#bdbdbd"/><circle cx="11" cy="6" r="1.6" fill="#fff"/><path d="M9 9.5h3v7h1.5" stroke="#fff" stroke-width="2" fill="none"/></svg></div>
      <div class="field"><label>How will this make their life/job easier/better?</label><div class="input"></div><svg class="info" width="22" height="22" viewBox="0 0 22 22"><circle cx="11" cy="11" r="11" fill="#bdbdbd"/><circle cx="11" cy="6" r="1.6" fill="#fff"/><path d="M9 9.5h3v7h1.5" stroke="#fff" stroke-width="2" fill="none"/></svg></div>
    </div>
    <div class="submit">SUBMIT</div>
  </section>

  <footer class="footer">Copyright © 2017 Leafline.</footer>
</div>
</body>
</html>
```